Letterhead Design Project

Suno Terra Coaching Services

My info is
Darvel Casson-Pruett
darvel@sunoterracoaching.example
sunoterracoaching.example
555-314-7082

you can play with order of items. I've never had a letterhead before. Thank you!

```html
<!DOCTYPE html>
<html lang="en">
<head>
<meta charset="utf-8">
<title>Suno Terra Coaching Services — Letterhead</title>
<link href="https://fonts.googleapis.com/css2?family=Montserrat:wght@400;500;600&display=swap" rel="stylesheet">
<style>
  :root {
    --backdrop: #2a2a2a;
    --paper: #ffffff;
    --ink: #2e2e2e;
    --brand-red: #a3192e;
    --brand-orange: #e0921a;
    --brand-orange-deep: #d27f12;
    --signature-blue: #1d2f8f;
    --footer-text: #ffffff;
  }
  * { margin: 0; padding: 0; box-sizing: border-box; }
  html, body {
    width: 1200px; height: 900px; overflow: hidden;
    background: var(--backdrop);
  }
  .canvas {
    position: relative; width: 1200px; height: 900px;
    display: flex; align-items: center; justify-content: center;
  }
  .letterhead {
    position: relative; width: 665px; height: 860px;
    background: var(--paper);
    font-family: "Montserrat", Arial, sans-serif;
    color: var(--ink);
    overflow: hidden;
    box-shadow: 0 10px 30px rgba(0,0,0,.45);
  }
  .brand {
    position: absolute; top: 48px; left: 0; width: 100%;
    display: flex; align-items: center; justify-content: center; gap: 12px;
  }
  .brand-dot {
    width: 34px; height: 34px; border-radius: 50%;
    background: var(--brand-orange);
  }
  .brand-name {
    font-weight: 600; font-size: 17px; letter-spacing: .5px;
    color: var(--brand-red);
  }
  .letter-body {
    position: absolute; top: 262px; left: 98px; width: 470px;
    font-size: 10.5px; line-height: 15px; text-align: justify;
  }
  .letter-body p + p { margin-top: 15px; }
  .sign-off { position: absolute; top: 606px; left: 98px; }
  .signature {
    width: 170px; height: 34px; border-radius: 4px;
    background: linear-gradient(90deg, rgba(29,47,143,.18), rgba(29,47,143,.06));
  }
  .sign-role { margin-top: 4px; font-size: 12px; color: var(--ink); }
  .swoosh { position: absolute; inset: 0; width: 665px; height: 860px; }
  .contact-line {
    position: absolute; left: 30px; bottom: 18px;
    font-size: 11px; font-weight: 500; color: var(--footer-text);
    display: flex; gap: 14px; white-space: nowrap;
  }
  .contact-label { color: var(--brand-red); font-weight: 600; margin-right: 4px; }
</style>
</head>
<body>
<div class="canvas">
  <article class="letterhead">
    <header class="brand">
      <span class="brand-dot"></span>
      <span class="brand-name">Suno Terra Coaching Services</span>
    </header>

    <section class="letter-body">
      <p>Letterhead samples are a great way of deciding what kind of letterhead you want to design for you and your company. The internet has a ton of great letterhead samples to browse through. Whether you want something simple, with just a couple lines of text of your business information, or something decorative and stunning, with photos and logos on the top and bottom of the page, it will be easy to find what you want, because there are samples online for basically any type of letterhead you could want.</p>
      <p>Any business could easily benefit from browsing through some letterhead samples, if only to get an idea for what kind of letterhead their company might want. Letterheads are just one of the tools that a business professional could use to help increase their customer base, and to really be memorable to everyone they write a letter to. Letterhead is quite an effective tool for marketing and advertising, but because it's such a simple and well known idea, it is often unfairly overlooked. Make sure you don't make that mistake, and make some letterhead samples of your own today.</p>
      <p>Whether you want to get new customers to remember you and become part of your clientele, or you just want to send out friendly reminders to your existing clients, customizing your own letterhead samples can really help you out. Try out some letterhead samples and you will not regret it, and I'm sure you will add a new tool to your business' arsenal of networking, marketing, and advertising tools.</p>
    </section>

    <div class="sign-off">
      <div class="signature" role="img" aria-label="Handwritten signature of the company director"></div>
      <div class="sign-role">company director</div>
    </div>

    <svg class="swoosh" viewBox="0 0 665 860" aria-hidden="true">
      <path fill="var(--brand-orange)" d="M0 735 C260 745 500 690 665 545 L665 860 L0 860 Z"/>
      <path fill="var(--paper)" d="M0 752 C260 760 500 705 665 565 L665 576 C500 718 260 772 0 764 Z"/>
      <path fill="var(--brand-red)" d="M0 770 C260 778 500 722 665 585 L665 610 C500 745 260 795 0 792 Z"/>
      <path fill="var(--paper)" d="M0 798 C260 802 500 752 665 618 L665 625 C500 760 260 810 0 806 Z"/>
      <path fill="var(--brand-orange-deep)" opacity=".35" d="M0 806 C260 810 500 760 665 625 L665 860 L0 860 Z"/>
    </svg>

    <footer class="contact-line">
      <span><span class="contact-label">P</span>555-314-7082</span>
      <span><span class="contact-label">E</span>darvel@sunoterracoaching.example</span>
      <span><span class="contact-label">W</span>www.sunoterracoaching.example</span>
    </footer>
  </article>
</div>
</body>
</html>
```